Gestalten Sie ein tolles Selbstliebe-Buchcover
Design kam bei der Zielgruppe sehr gut an und war professionell umgesetzt. Die Kommunikation läuft zielgerichtet und nett und ich habe schnell alle Dateien bekommen, die ich brauche. Vielen Dank!
Hallo,
schön, dass Sie sich für diese Ausschreibung interessieren. Wir suchen ein Cover für unser Buch, das wir im Selbstverlag veröffentlichen werden.
Titel: Mondgarten am Nordufer
Untertitel 1: Wie du dich von negativen Gedanken befreist und eine liebevolle Beziehung zu dir selbst aufbaust
Untertitel Teil 2: 12 lebensverändernde Monate voller positiver Impulse und Liebe für dich
Das Buch soll (mehrheitlich) Frauen unterstützen, eine liebevolle Beziehung zu sich selbst aufzubauen, negative Gedanken loszulassen und innere Ruhe zu finden.
Aufgabenstellung
Wir sind für jegliche Vorschläge im Rahmen des Themas, der Samples und der Schieberegler offen.
Wichtig ist allerdings
- dass das Design selbst in der kleinen Ansicht (Suchergebnisse) auf Vendora klar hervorsticht, das heißt dort klar erkennbar und die Schrift sofort lesbar ist. Es muss in klein „wirken“, weil viele mit dem Handy auf Vendora shoppen und die Ansicht in den Suchergebnissen dort noch kleiner ist.
- dass das Design die gezielt Emotionen vermittelt
Optimal wäre es, wenn Ihr keine Mockups hochladet. Das macht es viel schwieriger, die Designs einzuschätzen und miteinander zu vergleichen.

```html
<!DOCTYPE html>
<html lang="de">
<head>
<meta charset="utf-8">
<title>Mondgarten am Nordufer – Buchcover</title>
<link rel="stylesheet" href="https://fonts.googleapis.com/css2?family=Kaushan+Script&family=Montserrat:wght@700;800&display=swap">
<style>
  :root {
    --mist: #eef7f5;
    --seafoam: #bfe2dc;
    --teal: #3fb3a6;
    --teal-deep: #1f9c8f;
    --ink: #121212;
    --white: #ffffff;
    --gold-light: #f7df86;
    --gold: #d9a93a;
    --gold-deep: #b58524;
  }
  html, body {
    margin: 0;
    padding: 0;
    overflow: hidden;
    background: var(--mist);
  }
  .cover {
    position: relative;
    width: 800px;
    height: 1200px;
    overflow: hidden;
  }
  .cover-background {
    position: absolute;
    inset: 0;
    background:
      radial-gradient(ellipse 60% 38% at 50% 38%, #fbfefd 0%, rgba(251,254,253,0) 100%),
      linear-gradient(180deg, #cdebe6 0%, #e4f4f1 35%, #cfeae5 70%, #a9d9d1 100%);
  }
  .watercolor-patch {
    position: absolute;
    left: 0;
    top: 0;
    width: 800px;
    height: 1200px;
  }
  .author {
    position: absolute;
    top: 48px;
    left: 0;
    width: 800px;
    text-align: center;
    font-family: "Montserrat", sans-serif;
    font-weight: 800;
    font-size: 25px;
    letter-spacing: 0.55em;
    color: var(--ink);
    margin: 0;
  }
  .title {
    position: absolute;
    top: 190px;
    left: 0;
    width: 800px;
    margin: 0;
    text-align: center;
    font-family: "Kaushan Script", cursive;
    font-weight: 400;
  }
  .title-main {
    display: block;
    font-size: 128px;
    line-height: 1.25;
    background: linear-gradient(100deg, var(--gold-deep) 0%, var(--gold-light) 35%, var(--gold) 60%, var(--gold-deep) 100%);
    -webkit-background-clip: text;
    background-clip: text;
    color: transparent;
  }
  .title-sub {
    display: block;
    font-size: 104px;
    line-height: 1.2;
    color: var(--ink);
  }
  .subtitle {
    position: absolute;
    top: 640px;
    left: 130px;
    width: 540px;
    margin: 0;
    text-align: center;
    font-family: "Kaushan Script", cursive;
    font-size: 33px;
    line-height: 1.3;
    color: var(--white);
  }
  .promo-band {
    position: absolute;
    left: 0;
    top: 0;
    width: 800px;
    height: 1200px;
  }
  .promo-text {
    position: absolute;
    left: 544px;
    top: 1070px;
    width: 520px;
    margin: 0;
    transform: translate(-50%, -50%) rotate(-28deg);
    text-align: center;
    font-family: "Montserrat", sans-serif;
    font-weight: 700;
    font-size: 24px;
    line-height: 1.08;
    text-transform: uppercase;
    color: var(--ink);
  }
</style>
</head>
<body>
<main class="cover">
  <div class="cover-background" role="img" aria-label="Aquarellhintergrund in hellem Mint mit zarten Blattmotiven und Goldsprenkeln"></div>

  <svg class="watercolor-patch" viewBox="0 0 800 1200" role="img" aria-label="Türkisfarbener Aquarellfleck hinter dem Untertitel">
    <defs>
      <linearGradient id="patch-fill" x1="0" y1="0" x2="0" y2="1">
        <stop offset="0" stop-color="var(--teal-deep)" stop-opacity="0.85"/>
        <stop offset="0.55" stop-color="var(--teal)" stop-opacity="0.7"/>
        <stop offset="1" stop-color="var(--teal)" stop-opacity="0.15"/>
      </linearGradient>
    </defs>
    <path d="M150 600 Q300 570 600 556 L612 600 Q650 610 690 640 L735 690 Q760 760 745 830 Q600 860 400 850 Q200 860 60 830 Q40 760 70 700 Q110 660 140 650 Z" fill="url(#patch-fill)"/>
  </svg>

  <p class="author">LUIS VORINGER</p>

  <h1 class="title">
    <span class="title-main">Mondgarten</span>
    <span class="title-sub">am Nordufer</span>
  </h1>

  <p class="subtitle">Wie du dich von negativen Gedanken befreist und eine liebevolle Beziehung zu dir selbst aufbaust</p>

  <svg class="promo-band" viewBox="0 0 800 1200" aria-hidden="true">
    <defs>
      <linearGradient id="band-gold" x1="0" y1="1" x2="1" y2="0">
        <stop offset="0" stop-color="var(--gold-deep)"/>
        <stop offset="0.35" stop-color="var(--gold-light)"/>
        <stop offset="0.7" stop-color="var(--gold)"/>
        <stop offset="1" stop-color="var(--gold-deep)"/>
      </linearGradient>
    </defs>
    <polygon points="92,1200 800,828 800,1005 420,1200" fill="url(#band-gold)"/>
  </svg>

  <p class="promo-text">12 lebensverändernde<br>Monate voller positiver im<br>Pulse und Liebe für dich</p>
</main>
</body>
</html>
```